Thank You For Shopping / Hair Care Tips

I need “Thank You For Shopping”
Post cards made for my hair business !
I added pictures of post cards that I really like . I also added my LuzeKora Wigs logo for you guys to use

I want the backside of the flyer to have hair care tips !
I want people to have full directions on how to care for their wigs

Target Market(s)

Im marking to young woman to older middle aged woman
Ages 23-66 . I want my flyer to look mature And classy

Industry/Entity Type

Hair And Beauty

Font styles to use
Serif
Script

Colors
e34699
e34298
e34398

Requirements
Must have
• The flyer must have the Instagram logo with my Instagram name next to it @luze.kora.wigs__
• Also it must have my “Luze Kora Wigs” logo that I’ve uploaded in the pictures section .
• Flyer had to be two sides . One side “ thank you for shopping “ side two “hair care tips”
• My website must be on the flyer - www.luzekorawigs.example
• The flyer must match the colors of my logo
• All white . With the pink and glitter sliver you see on my logo
Nice to have
• Nice to have a glitter border
Should not have
• The flyer should not have different colors that don’t match my logo
• It shouldn’t be made without having my Instagram or website on the flyer

```html
<!DOCTYPE html>
<html lang="en">
<head>
<meta charset="utf-8">
<title>LuzeKora Wigs – Thank You Postcard</title>
<link rel="stylesheet" href="https://fonts.googleapis.com/css2?family=Josefin+Sans:wght@300;400&family=Mrs+Saint+Delafield&display=swap">
<style>
  :root {
    --pink: #f22ee8;
    --ink: #1e1e1e;
    --paper: #ffffff;
    --glitter-dark: #5f6a68;
    --glitter-light: #aab3b1;
  }
  * { margin: 0; padding: 0; box-sizing: border-box; }
  html, body { width: 1200px; height: 787px; overflow: hidden; background: var(--paper); }
  .canvas { position: relative; width: 1200px; height: 787px; background: var(--paper); }
  .card {
    position: absolute; top: 197px; width: 554px; height: 393px;
    background: radial-gradient(ellipse at 30% 20%, var(--glitter-light), var(--glitter-dark) 70%);
  }
  .card--front { left: 39px; }
  .card--back { left: 606px; }
  .card__panel {
    position: absolute; left: 15px; top: 16px; right: 16px; bottom: 16px;
    background: var(--paper); border: 3px solid var(--pink);
  }
  .brand {
    position: absolute; left: 20px; top: 40px;
    font-family: "Josefin Sans", sans-serif; font-weight: 400;
    font-size: 26px; letter-spacing: 1px; color: var(--pink);
  }
  .thanks {
    position: absolute; left: 140px; top: 120px; width: 260px;
    font-family: "Mrs Saint Delafield", cursive; font-size: 72px;
    line-height: 62px; color: var(--pink); text-align: center;
  }
  .website {
    position: absolute; left: 0; right: 0; bottom: 18px; text-align: center;
    font-family: "Josefin Sans", sans-serif; font-weight: 400;
    font-size: 11px; letter-spacing: 0.6px; color: var(--ink);
  }
  .social {
    position: absolute; right: 8px; top: 14px; display: flex; align-items: center; gap: 6px;
    font-family: "Josefin Sans", sans-serif; font-weight: 300;
    font-size: 11px; color: var(--pink); text-transform: uppercase;
  }
  .social__dot { width: 13px; height: 13px; border-radius: 50%; background: var(--pink); }
  .tips-title {
    position: absolute; left: 0; right: 0; top: 34px; text-align: center;
    font-family: "Mrs Saint Delafield", cursive; font-size: 58px;
    line-height: 50px; color: var(--pink);
  }
  .tips {
    position: absolute; left: 0; right: 0; top: 99px; list-style: none; text-align: center;
    font-family: "Josefin Sans", sans-serif; font-weight: 300;
    font-size: 9.6px; line-height: 10.6px; color: var(--ink); letter-spacing: 0.3px;
  }
  .tips li { margin-bottom: 10.6px; }
</style>
</head>
<body>
<main class="canvas">
  <section class="card card--front" role="img" aria-label="Silver glitter border around the thank-you card">
    <div class="card__panel">
      <div class="brand">LuzeKora Wigs</div>
      <h1 class="thanks">thank you for shopping</h1>
      <p class="website">WWW.LUZEKORAWIGS.EXAMPLE</p>
    </div>
  </section>

  <section class="card card--back" role="img" aria-label="Silver glitter border around the hair care tips card">
    <div class="card__panel">
      <div class="social"><span class="social__dot"></span>@luze.kora.wigs__</div>
      <h2 class="tips-title">Hair care tips</h2>
      <ul class="tips">
        <li>Apply a rich &amp; moisturising conditioner and comb the<br>hair, starting with the ends working your way up</li>
        <li>Leave the conditioner in for at least<br>15 minutes or more</li>
        <li>Do not massage the hair</li>
        <li>Rinse throughout</li>
        <li>Gently scrunch the hair to enchance it's curls</li>
        <li>When damp, apply a small amount<br>of anti-frizz hair serum</li>
        <li>Let it air-dry</li>
        <li>Do not use oil product or excessive products<br>on curly hair, it will cause matting.</li>
        <li>Do not brush or comb hair when dry, it will<br>cause hair to frizz and may tangle the hair</li>
      </ul>
    </div>
  </section>
</main>
</body>
</html>
```